Adventurous female pilot

I am looking for a personal business card, for a very well qualified female pilot, with a lot of aviation experience.

Currently an airline pilot, have worked as a bush pilot in Africa, looking to get into corporate aviation, or private jet owners.
Want a classy looking card for networking...

Could be interested in a retro\vintage look also?!

An idea,, is an african sunset background, with my wings\logo on it
Updates

I just want to say thank you to all of your for your amazing designs!

I have been very busy flying this past week , so not had a chance to be on the computer much.
But I provide some feedback, and conclusions very soon!
Thank you again.

Marla

Reason: Still waiting on a couple of revisions to be 100% about my choice!

Target Market(s)

corporate aviation, private jet owners, casino's,
General audience.
networking

Industry/Entity Type

Airline

Requirements
Nice to have
• Classy, edgy, sexy, but also feminine

```html
<!DOCTYPE html>
<html lang="en">
<head>
<meta charset="utf-8">
<title>Marla Vance Aviation – Business Card</title>
<link rel="stylesheet" href="https://fonts.googleapis.com/css2?family=Questrial&family=Arimo:ital,wght@1,700&display=swap">
<style>
  :root {
    --backdrop: #121312;
    --pink: #e3166e;
    --pink-deep: #c80f5c;
    --pink-glow: #f6a3c5;
    --silver: #b9bcc0;
    --silver-light: #f1f2f3;
    --ink: #1e1e1e;
    --ink-soft: #6a6a6a;
    --white: #ffffff;
    --card-back: #050607;
  }
  html, body {
    margin: 0;
    padding: 0;
    width: 1200px;
    height: 1200px;
    overflow: hidden;
    background: var(--backdrop);
  }
  .stage {
    position: relative;
    width: 1200px;
    height: 1200px;
  }
  .card {
    position: absolute;
    top: 440px;
    width: 534px;
    height: 320px;
    display: block;
  }
  .card--front { left: 47px; }
  .card--back { left: 620px; }
  .card-text {
    font-family: "Questrial", "Century Gothic", sans-serif;
  }
  .owner-name { fill: var(--ink); font-size: 17px; letter-spacing: 0.3px; }
  .owner-field { fill: var(--ink-soft); font-size: 12.5px; letter-spacing: 0.5px; }
  .contact-line { fill: var(--white); font-size: 15px; letter-spacing: 0.4px; }
  .web-address {
    font-family: "Arimo", Arial, sans-serif;
    font-style: italic;
    font-weight: 700;
    font-size: 12.5px;
    letter-spacing: 1px;
    fill: var(--white);
  }
</style>
</head>
<body>
<main class="stage">

  <!-- Front face -->
  <svg class="card card--front" viewBox="0 0 534 320" role="group" aria-label="Front of business card">
    <defs>
      <radialGradient id="front-bg" cx="50%" cy="20%" r="85%">
        <stop offset="0%" stop-color="#ef3d88"/>
        <stop offset="55%" stop-color="var(--pink)"/>
        <stop offset="100%" stop-color="var(--pink-deep)"/>
      </radialGradient>
      <radialGradient id="halo" cx="50%" cy="50%" r="50%">
        <stop offset="0%" stop-color="var(--pink-glow)" stop-opacity="0.9"/>
        <stop offset="100%" stop-color="var(--pink-glow)" stop-opacity="0"/>
      </radialGradient>
      <linearGradient id="plate" x1="0" y1="0" x2="0" y2="1">
        <stop offset="0%" stop-color="#ffffff"/>
        <stop offset="70%" stop-color="#f3f3f4"/>
        <stop offset="100%" stop-color="#dcdde0"/>
      </linearGradient>
      <linearGradient id="rim" x1="0" y1="0" x2="1" y2="1">
        <stop offset="0%" stop-color="var(--silver-light)"/>
        <stop offset="50%" stop-color="var(--silver)"/>
        <stop offset="100%" stop-color="#8e9196"/>
      </linearGradient>
      <clipPath id="front-clip"><rect width="534" height="320"/></clipPath>
    </defs>
    <g clip-path="url(#front-clip)">
      <rect class="card-surface" width="534" height="320" fill="url(#front-bg)"/>
      <ellipse class="plate-halo" cx="267" cy="150" rx="230" ry="50" fill="url(#halo)"/>
      <ellipse class="name-plate" cx="267" cy="-4" rx="208" ry="196" fill="url(#plate)" stroke="url(#rim)" stroke-width="5"/>
      <circle class="brand-dot" cx="267" cy="72" r="26" fill="#c9cacd"/>
      <text class="card-text owner-name" x="267" y="159" text-anchor="middle">MARLA VANCE</text>
      <text class="card-text owner-field" x="267" y="175" text-anchor="middle">AVIATION</text>
      <text class="card-text contact-line" x="267" y="221" text-anchor="middle">dummy  dummy, dummy</text>
      <text class="card-text contact-line" x="267" y="239" text-anchor="middle">dummy City dummy</text>
      <text class="card-text contact-line" x="267" y="270" text-anchor="middle">+63 900 5550123  |  (083) 555019</text>
      <text class="card-text contact-line" x="267" y="288" text-anchor="middle">hello@marlavance.com  |  www.marlavance.com</text>
    </g>
  </svg>

  <!-- Back face -->
  <svg class="card card--back" viewBox="0 0 534 320" role="group" aria-label="Back of business card">
    <defs>
      <radialGradient id="gem" cx="50%" cy="45%" r="55%">
        <stop offset="0%" stop-color="#d0166a"/>
        <stop offset="70%" stop-color="#a70e52"/>
        <stop offset="100%" stop-color="#6e0634"/>
      </radialGradient>
      <radialGradient id="gem-glow" cx="50%" cy="50%" r="50%">
        <stop offset="75%" stop-color="#ffffff" stop-opacity="0.35"/>
        <stop offset="100%" stop-color="#ffffff" stop-opacity="0"/>
      </radialGradient>
      <linearGradient id="ring" x1="0" y1="0" x2="1" y2="1">
        <stop offset="0%" stop-color="#ffffff"/>
        <stop offset="50%" stop-color="var(--silver)"/>
        <stop offset="100%" stop-color="#eceef0"/>
      </linearGradient>
      <linearGradient id="shine" x1="0" y1="0" x2="0" y2="1">
        <stop offset="0%" stop-color="#ffffff" stop-opacity="0.45"/>
        <stop offset="100%" stop-color="#ffffff" stop-opacity="0"/>
      </linearGradient>
    </defs>
    <rect class="card-surface" width="534" height="320" fill="var(--card-back)"/>
    <ellipse class="gem-glow" cx="266" cy="160" rx="104" ry="128" fill="url(#gem-glow)"/>
    <ellipse class="gem-ring" cx="266" cy="160" rx="90" ry="113" fill="url(#ring)"/>
    <ellipse class="gem-face" cx="266" cy="160" rx="83" ry="106" fill="url(#gem)"/>
    <ellipse class="gem-shine" cx="258" cy="112" rx="62" ry="50" fill="url(#shine)"/>
    <text class="web-address" x="266" y="164" text-anchor="middle">www.marlavance.com</text>
  </svg>

</main>
</body>
</html>
```